American pesto sauce company needs a vintage/ old fashioned package design

Company name: Marisol Grove.
We need a food label design for 4 different flavors of pesto sauce: classic almond, sundried tomato, roasted red pepper, and Cajun spice. For those that do not know what pesto is, it is a sauce like tomato sauce that is traditionally Italian and goes on pasta or whatever you choose to put it on and the consistent ingredients are garlic, cheese, nuts, olive oil and basil. They are fresh, all natural without preservatives, artificial flavors or colors.
The design of the jar is an old fashioned wire bale jar used for preserving foods ( attached is a picture). I'm looking for a label with:
• an upscale vintage feel but will also stand out on a grocery store shelf. I have attached an example of the feel I am looking for as well as the format of the words with my company name.
• The word "Pesto" must be prominent on the label.
• metalic gold boarders that go around the whole label maybe with gold embellishments if you see fit for that upscale feeling.
• Also, as you can see in the attachment, there are different typesets. And it must be easy to read from at least 3 feet away.
• Each label will have a different color corresponding to the flavor- could be part of the flavor text
• The bottom of the front panel must have “Net Wt. 5.75 oz (162g)” in a creative format how you see fit. Measures: height-28 mm, width-75mm
• Need logo for top part of label with the letters MG for Marisol Grove and it will also contain the website, address and parent company name, use by date, etc. Measures:50 mm diameter
• The back panel of the label will contain the nutrition facts, ingredients and bar code. Measures: height-28 mm, width-75mm

Also the label is one piece with 3 different sections. Attached will be an example with measurements.
Updates

Check out this website on packaging. I absolutely love love love the Hartwell Pantry almond water labels. The colors for the different flavors. How its not just horizontal or vertical. The different typesets/fonts/typography. The flourishes and background thats faded.
http://brightwrapgallery.com/page/3/

Target Market(s)

Target market is medium- high income foodies between 35-65

Industry/Entity Type

Grocery Store

Requirements
Must have
• Net Wt on front lower panel. Separation of the company name Marisol & Pesto. See attachment.
Nice to have
• Name of flavor designed in a wave pattern as shown in attachment. Hand drawn font OK.

```html
<!DOCTYPE html>
<html lang="en">
<head>
<meta charset="utf-8">
<title>Marisol Grove Pesto Labels</title>
<link href="https://fonts.googleapis.com/css2?family=Fjalla+One&family=Playfair+Display:wght@400;700&family=Arimo:wght@400&display=swap" rel="stylesheet">
<style>
  :root{
    --page:#ffffff;
    --cream:#efe6c6;
    --cream-deep:#e2d3a4;
    --gold:#c9a94f;
    --gold-light:#e6cf87;
    --gold-dark:#9b7c33;
    --lid-green:#1d7a4b;
    --tab-black:#111111;
    --ink:#2b2115;
    --brown-frame:#3a2615;
    --teal-frame:#2d7f74;
    --ribbon-red:#b8321f;
    --ribbon-red-dark:#7e1e12;
    --ribbon-green:#2f7d3f;
    --ribbon-green-dark:#1b5a2a;
    --ribbon-text:#f3ead0;
  }
  *{margin:0;padding:0;box-sizing:border-box}
  html,body{width:1200px;height:885px;overflow:hidden;background:var(--page)}
  .label-sheet{width:1200px;height:885px;display:flex;justify-content:center;gap:120px;padding-top:30px}
  .label-set{width:460px;position:relative;height:830px}

  .lid-seal{position:absolute;left:120px;top:0;width:220px;height:220px}
  .lid-seal svg{display:block}
  .lid-text{position:absolute;inset:0;display:flex;flex-direction:column;align-items:center;justify-content:center;
    font-family:"Arimo",sans-serif;color:var(--cream);text-align:center;line-height:1.35}
  .lid-text .lid-mark{font-family:"Fjalla One",sans-serif;font-size:40px;line-height:44px;letter-spacing:2px}
  .lid-text .lid-brand{font-family:"Fjalla One",sans-serif;font-size:18px;letter-spacing:1px;margin-bottom:4px}
  .lid-text .lid-line{font-size:11px;letter-spacing:.5px}

  .side-tab{position:absolute;left:195px;top:232px;width:70px;height:168px;background:var(--tab-black);
    border-radius:0 0 6px 6px;display:flex;align-items:center;justify-content:center}
  .side-tab span{transform:rotate(-90deg);font-family:"Fjalla One",sans-serif;font-size:30px;color:var(--cream);white-space:nowrap}

  .front-panel{position:absolute;left:0;top:410px;width:460px;height:400px}
  .front-panel svg{position:absolute;inset:0}
  .panel-brand{position:absolute;left:0;right:0;top:52px;text-align:center;font-family:"Fjalla One",sans-serif;font-size:28px;color:var(--ink)}
  .panel-flavor{position:absolute;left:0;right:0;top:92px;text-align:center;font-family:"Fjalla One",sans-serif;
    font-size:44px;line-height:46px;color:var(--ink);text-transform:uppercase;letter-spacing:.5px}
  .panel-pesto{position:absolute;left:0;right:0;top:211px;text-align:center;font-family:"Playfair Display",serif;
    font-size:36px;line-height:44px;color:var(--ribbon-text);letter-spacing:1px}
  .panel-weight{position:absolute;left:0;right:0;top:330px;text-align:center;font-family:"Arimo",sans-serif;
    font-size:22px;color:var(--ink);letter-spacing:1px}
</style>
</head>
<body>
<main class="label-sheet">

  <section class="label-set flavor-tomato">
    <div class="lid-seal">
      <svg width="220" height="220" viewBox="0 0 220 220">
        <circle cx="110" cy="110" r="108" fill="var(--gold)"/>
        <circle cx="110" cy="110" r="98" fill="var(--gold-dark)"/>
        <circle cx="110" cy="110" r="92" fill="var(--lid-green)"/>
        <circle cx="110" cy="110" r="84" fill="none" stroke="var(--gold-light)" stroke-width="1.5"/>
      </svg>
      <div class="lid-text">
        <span class="lid-mark">MG</span>
        <span class="lid-brand">Marisol Grove</span>
        <span class="lid-line">All Natural Pesto</span>
        <span class="lid-line">Use By Date</span>
      </div>
    </div>
    <div class="side-tab"><span>Marisol</span></div>
    <div class="front-panel">
      <svg width="460" height="400" viewBox="0 0 460 400">
        <defs>
          <linearGradient id="paper-a" x1="0" y1="0" x2="1" y2="1">
            <stop offset="0" stop-color="var(--cream)"/><stop offset=".5" stop-color="var(--cream-deep)"/><stop offset="1" stop-color="var(--cream)"/>
          </linearGradient>
        </defs>
        <rect width="460" height="400" fill="var(--cream)"/>
        <rect x="5" y="5" width="450" height="390" fill="none" stroke="var(--gold)" stroke-width="6"/>
        <rect x="14" y="14" width="432" height="372" fill="none" stroke="var(--gold-dark)" stroke-width="1.5"/>
        <path d="M62 30 H398 A22 22 0 0 0 420 52 V288 A22 22 0 0 0 398 310 H62 A22 22 0 0 0 40 288 V52 A22 22 0 0 0 62 30 Z"
              fill="url(#paper-a)" stroke="var(--brown-frame)" stroke-width="6" role="img" aria-label="Faded vintage paper texture"/>
        <path d="M70 40 H390 A20 20 0 0 0 410 60 V280 A20 20 0 0 0 390 300 H70 A20 20 0 0 0 50 280 V60 A20 20 0 0 0 70 40 Z"
              fill="none" stroke="var(--gold)" stroke-width="2.5"/>
        <polygon points="62,224 122,224 122,266 62,266 80,245" fill="var(--ribbon-red-dark)"/>
        <polygon points="398,224 338,224 338,266 398,266 380,245" fill="var(--ribbon-red-dark)"/>
        <rect x="110" y="210" width="240" height="46" fill="var(--ribbon-red)" stroke="var(--gold)" stroke-width="2"/>
      </svg>
      <div class="panel-brand">Marisol</div>
      <div class="panel-flavor">Sundried<br>Tomato</div>
      <div class="panel-pesto">PESTO</div>
      <div class="panel-weight">Net Wt. 5.75 oz (162g)</div>
    </div>
  </section>

  <section class="label-set flavor-pepper">
    <div class="lid-seal">
      <svg width="220" height="220" viewBox="0 0 220 220">
        <circle cx="110" cy="110" r="108" fill="var(--gold)"/>
        <circle cx="110" cy="110" r="98" fill="var(--gold-dark)"/>
        <circle cx="110" cy="110" r="92" fill="var(--lid-green)"/>
        <circle cx="110" cy="110" r="84" fill="none" stroke="var(--gold-light)" stroke-width="1.5"/>
      </svg>
      <div class="lid-text">
        <span class="lid-mark">MG</span>
        <span class="lid-brand">Marisol Grove</span>
        <span class="lid-line">All Natural Pesto</span>
        <span class="lid-line">Use By Date</span>
      </div>
    </div>
    <div class="side-tab"><span>Marisol</span></div>
    <div class="front-panel">
      <svg width="460" height="400" viewBox="0 0 460 400">
        <defs>
          <linearGradient id="paper-b" x1="0" y1="0" x2="1" y2="1">
            <stop offset="0" stop-color="var(--cream)"/><stop offset=".5" stop-color="var(--cream-deep)"/><stop offset="1" stop-color="var(--cream)"/>
          </linearGradient>
        </defs>
        <rect width="460" height="400" fill="var(--cream)"/>
        <rect x="5" y="5" width="450" height="390" fill="none" stroke="var(--gold)" stroke-width="6"/>
        <rect x="14" y="14" width="432" height="372" fill="none" stroke="var(--gold-dark)" stroke-width="1.5"/>
        <path d="M62 30 H398 A22 22 0 0 0 420 52 V288 A22 22 0 0 0 398 310 H62 A22 22 0 0 0 40 288 V52 A22 22 0 0 0 62 30 Z"
              fill="url(#paper-b)" stroke="var(--teal-frame)" stroke-width="6" role="img" aria-label="Faded vintage paper texture"/>
        <path d="M70 40 H390 A20 20 0 0 0 410 60 V280 A20 20 0 0 0 390 300 H70 A20 20 0 0 0 50 280 V60 A20 20 0 0 0 70 40 Z"
              fill="none" stroke="var(--gold)" stroke-width="2.5"/>
        <polygon points="62,224 122,224 122,266 62,266 80,245" fill="var(--ribbon-green-dark)"/>
        <polygon points="398,224 338,224 338,266 398,266 380,245" fill="var(--ribbon-green-dark)"/>
        <rect x="110" y="210" width="240" height="46" fill="var(--ribbon-green)" stroke="var(--gold)" stroke-width="2"/>
      </svg>
      <div class="panel-brand">Marisol</div>
      <div class="panel-flavor">Roasted Red<br>Pepper</div>
      <div class="panel-pesto">PESTO</div>
      <div class="panel-weight">Net Wt. 5.75 oz (162g)</div>
    </div>
  </section>

</main>
</body>
</html>
```